Word template Letterhead for Australian Law Firm

We are a small law firm based in Manly, NSW, Australia. We have had a new logo designed for us and wish to freshen up the appearance of our letterhead. We require the letterhead to be in a word document that we can type over. This will not be a ‘printed’ letterhead because we send the majority of our correspondence via email. We would like to see a few options. We have attached our previous letterhead as well as the artwork for our new logo. We like the idea of a watermark across the bottom of the letter but the watermark must stay in place and we must be able to type over it. We are open to some colour throughout the letterhead because the majority of our correspondence is sent electronically. We also use electronic signatures. I have uploaded an example of this.The letterhead must include:-1. Our address details – including our phone number, physical address, website address etc. These details can be found on the copy of our previous letterhead;2. ABN Number;3. The words ‘Brevicor (NSW) Pty Ltd ACN 482 731 058 trading as Shipton & AssociatesLiability limited by a scheme approved under Professional Standards Legislation. The letterhead does not need to include the names and qualifications of the people working at the firm. Thank you.

Target Market(s)

Clients and other parties

Industry/Entity Type

Law Firm

Font styles to use
Other font styles liked:
• raleway, montserrat

Colors

Designer to choose colors to be used in the design.

Requirements
Must have
• Certain wording - please see project description.
• Must be a word document and must be able to type over the watermark etc.
Nice to have
• Watermark at the bottom of the letter.

```html
<!DOCTYPE html>
<html lang="en">
<head>
<meta charset="utf-8">
<title>Kervell &amp; Associates Letterhead</title>
<link href="https://fonts.googleapis.com/css2?family=Montserrat:wght@400;600;700&family=Raleway:wght@400;500&display=swap" rel="stylesheet">
<style>
:root{
  --navy:#2b3a8c;
  --blue:#5f72b8;
  --gold:#b8a36a;
  --ink:#2a2a2e;
  --muted:#55565c;
  --paper:#ffffff;
  --backdrop:#ececee;
}
*{margin:0;padding:0;box-sizing:border-box}
html,body{width:1200px;height:795px;overflow:hidden;background:var(--backdrop)}
.letterhead{position:absolute;left:320px;top:14px;width:560px;height:767px;background:var(--paper);
  box-shadow:0 2px 10px rgba(0,0,0,.08);font-family:"Raleway",Arial,sans-serif;color:var(--ink);overflow:hidden}
.firm-details{position:absolute;right:38px;top:34px;width:230px;font-size:6.4px;line-height:1.55;color:var(--muted)}
.firm-details .firm-title{font-family:"Montserrat",Arial,sans-serif;font-weight:700;font-size:8.5px;letter-spacing:2.4px;color:var(--ink);
  padding-bottom:4px;border-bottom:1px dotted var(--gold);margin-bottom:4px}
.firm-details b{font-family:"Montserrat",Arial,sans-serif;font-weight:700;color:var(--ink)}
.brand{position:absolute;left:40px;top:120px;display:flex;align-items:center;gap:8px}
.brand-dot{width:26px;height:26px;border-radius:50%;background:var(--navy)}
.brand-name{font-family:"Montserrat",Arial,sans-serif;font-weight:700;font-size:13px;color:var(--navy);letter-spacing:.3px}
.watermark{position:absolute;left:170px;top:230px;width:230px;height:230px;border-radius:50%;background:var(--blue);opacity:.08}
.accreditation{position:absolute;right:60px;top:245px;width:52px;height:52px;border-radius:50%;border:2px solid var(--navy);background:#dbe7f5}
.letter{position:absolute;left:60px;top:175px;width:400px;font-size:8.6px;line-height:1.6}
.salutation{margin-bottom:14px}
.letter p{margin-bottom:10px}
.sign-off{position:absolute;left:60px;top:500px;font-size:8.6px;line-height:1.5}
.signature-line{display:block;width:60px;height:22px;margin:4px 0}
.footer-legal{position:absolute;right:38px;bottom:26px;width:300px;font-size:6px;line-height:1.5;color:var(--muted);text-align:right;
  padding-top:5px;border-top:1px solid;border-image:linear-gradient(90deg,var(--gold) 50%,var(--navy) 50%) 1}
.edge-band{position:absolute;left:0;right:0;bottom:0;height:7px;background:linear-gradient(90deg,var(--gold) 50%,var(--navy) 50%)}
</style>
</head>
<body>
<main class="letterhead">
  <section class="firm-details">
    <div class="firm-title">KERVELL &amp; ASSOCIATES</div>
    <div>Suite 4, 18 Tidewater Lane, HARBOURVALE NSW 2107</div>
    <div><b>TEL:</b> (02) 9411 3870 | <b>EMAIL:</b> reception@brevicorlaw.com.au</div>
    <div><b>FACSIMILE:</b> (02) 9411 3871 | www.kervellassociates.com.au</div>
    <div><b>OUR REF:</b> CN:HC:7930 | <b>YOUR REF:</b> Dean Halloway</div>
    <div><b>ABN:</b> 83 482 731 058</div>
  </section>

  <div class="brand">
    <span class="brand-dot"></span>
    <span class="brand-name">Kervell &amp; Associates</span>
  </div>

  <div class="watermark" role="img" aria-label="Faint firm watermark"></div>
  <div class="accreditation" role="img" aria-label="Accredited specialist badge"></div>

  <article class="letter">
    <p class="salutation">Dear Sir/Madam</p>
    <p>Lorem Ipsum is simply dummy text of the printing and typesetting industry. Lorem Ipsum has been the industry's standard dummy text ever since the 1500s, when an unknown printer took a galley of type and scrambled it to make a type specimen book. It has survived not only five centuries, but also the leap into electronic typesetting, remaining essentially unchanged. It was popularised in the 1960s with the release of Letraset sheets containing Lorem Ipsum passages, and more recently with desktop publishing software like Aldus PageMaker including versions of Lorem Ipsum.</p>
    <p>It is a long established fact that a reader will be distracted by the readable content of a page when looking at its layout. The point of using Lorem Ipsum is that it has a more-or-less normal distribution of letters, as opposed to using 'Content here, content here', making it look like readable English. Many desktop publishing packages and web page editors now use Lorem Ipsum as their default model text, and a search for 'lorem ipsum' will uncover many web sites still in their infancy. Various versions have evolved over the years, sometimes by accident, sometimes on purpose (injected humour and the like).</p>
    <p>Regards,</p>
  </article>

  <div class="sign-off">
    <div>Yours faithfully</div>
    <div>KERVELL &amp; ASSOCIATES</div>
    <svg class="signature-line" viewBox="0 0 60 22"><path d="M4 16 C12 4 16 20 22 10 S32 16 38 8 S50 14 56 10" fill="none" stroke="#333" stroke-width="1"/></svg>
    <div>HANNAH CORBETT</div>
    <div>Direct Email: hannah@brevicorlaw.com.au</div>
  </div>

  <footer class="footer-legal">
    Brevicor (NSW) Pty Ltd ACN 482 731 058 trading as Kervell &amp; Associates.<br>
    Liability limited by a scheme approved under Professional Standards Legislation. Legal practitioners at<br>
    Brevicor (NSW) Pty Ltd are members of the scheme.
  </footer>
  <div class="edge-band"></div>
</main>
</body>
</html>
```